Flyer-Design für  Kampfsportschule
Flyer-Design für Kampfsportschule
Zielgruppe
Wir bieten Taekwondo/Selbstverteidigung an. Meine Zielgruppe sind Erwachsene ab 17 Jahren.
Aufgabenstellung
Das Angebot '1 Monat kostenloses Training, oder einen Monat kostenloses Training' und 'Taekwondo/Selbstverteidigung in Weinstadt' soll eingebracht und direkt sichtbar sein. Eventuell auch Punkte wie Selbstbewusstsein, Beweglichkeit, Zielstrebigkeit, Kraft und Ausdauer, körperliche Fitness... Farben: Weiß, schwarz und Schrift in gelb. Nichts rotes.
Die Daten:
Tel: 0159-4817250 Email: t.m.budohalle@postwelle-mail.de und www.tmbudohalle.de

```html
<!DOCTYPE html>
<html lang="de">
<head>
<meta charset="utf-8">
<title>T.M. Budohalle – Flyer Selbstverteidigung</title>
<link rel="stylesheet" href="https://fonts.googleapis.com/css2?family=Raleway:wght@700;800&family=Open+Sans:wght@600;700;800&display=swap">
<style>
  :root {
    --page-bg: #f4f4f4;
    --flyer-black: #141414;
    --flyer-black-soft: #232323;
    --accent-yellow: #f5c518;
    --text-white: #ffffff;
    --text-black: #111111;
    --photo-light: #d9d4cf;
    --photo-dark: #2a2624;
  }
  * { box-sizing: border-box; margin: 0; padding: 0; }
  html, body {
    width: 1200px; height: 817px; overflow: hidden;
    background: var(--page-bg);
  }
  .canvas {
    width: 1200px; height: 817px;
    display: flex; align-items: center; justify-content: center;
  }
  .flyer {
    position: relative;
    width: 380px; height: 775px;
    background:
      radial-gradient(ellipse at 30% 20%, var(--flyer-black-soft), transparent 60%),
      radial-gradient(ellipse at 70% 70%, #1d1d1d, transparent 55%),
      var(--flyer-black);
    overflow: hidden;
    font-family: "Open Sans", sans-serif;
    color: var(--text-white);
    box-shadow: 0 6px 18px rgba(0,0,0,0.18);
  }
  .brand {
    position: absolute; top: 48px; left: 0; right: 0;
    display: flex; align-items: center; justify-content: center; gap: 10px;
    height: 110px;
  }
  .brand-dot {
    width: 18px; height: 18px; border-radius: 50%;
    background: var(--accent-yellow);
  }
  .brand-name {
    font-weight: 800; font-size: 22px; letter-spacing: 0.5px;
    color: var(--text-white);
  }
  .headline {
    position: absolute; top: 178px; left: 0; right: 0;
    text-align: center;
    font-family: "Raleway", sans-serif; font-weight: 700;
    font-size: 33px; line-height: 42px;
  }
  .headline .place { color: var(--accent-yellow); display: block; }
  .question {
    position: absolute; top: 272px; left: 30px; right: 24px;
    font-weight: 700; font-size: 14px; line-height: 22px;
  }
  .question .hl { color: var(--accent-yellow); }
  .benefits {
    position: absolute; top: 340px; left: 30px;
    list-style: none;
  }
  .benefits li {
    position: relative; padding-left: 22px;
    font-weight: 700; font-size: 13.5px; line-height: 27px;
  }
  .benefits li::before {
    content: ""; position: absolute; left: 0; top: 10px;
    width: 8px; height: 8px; border-radius: 50%;
    background: var(--accent-yellow);
  }
  .photo {
    position: absolute; left: 208px; top: 330px;
    width: 166px; height: 317px;
    background: linear-gradient(180deg, var(--photo-dark) 0%, #6f6a66 30%, var(--photo-light) 55%, #bdb7b1 85%, var(--photo-dark) 100%);
    border-radius: 60px 60px 0 0;
    opacity: 0.9;
  }
  .offer {
    position: absolute; left: 28px; top: 500px;
    width: 162px; height: 110px;
    border: 2px solid var(--accent-yellow);
    display: flex; flex-direction: column; align-items: center; justify-content: center;
    font-weight: 700; font-size: 21px; line-height: 28px; text-align: center;
  }
  .offer .months { color: var(--accent-yellow); }
  .contact-band {
    position: absolute; left: 0; right: 0; bottom: 0; height: 128px;
    background: var(--accent-yellow);
    color: var(--text-black);
    display: flex; align-items: center;
    padding: 0 16px 0 28px; gap: 28px;
  }
  .call {
    font-family: "Raleway", sans-serif; font-weight: 800;
    font-size: 22px; line-height: 28px;
  }
  .details {
    font-weight: 600; font-size: 10.5px; line-height: 20px;
  }
  .details b { font-weight: 800; }
</style>
</head>
<body>
<main class="canvas">
  <article class="flyer">
    <header class="brand">
      <span class="brand-dot"></span>
      <span class="brand-name">T.M. Budohalle</span>
    </header>

    <h1 class="headline">Selbstverteidigung<span class="place">in Weinstadt</span></h1>

    <p class="question">Was bekommen Sie, wenn Sie <span class="hl">Selbst-<br>verteidigung</span> lernen?</p>

    <ul class="benefits">
      <li>Selbstbewusstsein</li>
      <li>Beweglichkeit</li>
      <li>Selbstverteidigung</li>
      <li>Kraft und Ausdauer</li>
      <li>körperliche Fitness</li>
    </ul>

    <div class="photo" role="img" aria-label="Foto: Taekwondo-Kämpferin im weißen Dobok mit schwarzem Gürtel in Abwehrhaltung"></div>

    <div class="offer">
      <span class="months">1 Monat</span>
      <span>kostenloses</span>
      <span>Training</span>
    </div>

    <footer class="contact-band">
      <p class="call">Jetzt<br>anrufen!</p>
      <p class="details">
        <b>Tel:</b> 0159-4817250<br>
        t.m.budohalle@postwelle-mail.de<br>
        www.tmbudohalle.de
      </p>
    </footer>
  </article>
</main>
</body>
</html>
```